Layout for site fence advertising - length approx. 250 cm x 125 cm

The advertising will later be printed on a PVC film and used for events or on sports fields.

Main services :
Your regional contact at
Real estate and business financing
independent insurance advice

```html
<!DOCTYPE html>
<html lang="de">
<head>
<meta charset="utf-8">
<title>Nordtal Finanzberatung – Bauzaunbanner</title>
<link href="https://fonts.googleapis.com/css2?family=Montserrat:wght@300;500&family=Poppins:wght@600;700&display=swap" rel="stylesheet">
<style>
  :root {
    --brand-blue: #224b9c;
    --white: #ffffff;
    --stage: #e9ecf1;
    --photo-dark: #5a3a2e;
    --photo-light: #c9b9ae;
  }
  * { margin: 0; padding: 0; box-sizing: border-box; }
  html, body {
    width: 1117px; height: 1200px; overflow: hidden;
    background: var(--stage);
  }
  .banner {
    position: absolute; left: 0; top: 321px;
    width: 1117px; height: 558px;
    background: var(--brand-blue);
    overflow: hidden;
    color: var(--white);
  }
  .brand-mark {
    position: absolute; left: 52px; top: 53px;
    width: 120px; height: 120px;
    border: 4px solid var(--white); border-radius: 50%;
  }
  .brand-divider {
    position: absolute; left: 185px; top: 49px;
    width: 4px; height: 127px; background: var(--white);
  }
  .brand-name {
    position: absolute; left: 198px; top: 84px;
    font: 500 22px/1 "Montserrat", sans-serif;
    white-space: nowrap;
  }
  .brand-tagline {
    position: absolute; left: 197px; top: 115px;
    font: 500 17px/1 "Montserrat", sans-serif;
    white-space: nowrap;
  }
  .headline { font-family: "Poppins", sans-serif; font-weight: normal; }
  .headline-small {
    position: absolute; font: 700 33px/1 "Poppins", sans-serif;
    white-space: nowrap;
  }
  .headline-your { left: 87px; top: 208px; }
  .headline-regional {
    position: absolute; left: 64px; top: 229px;
    font: 300 70px/1 "Montserrat", sans-serif; letter-spacing: 0.3px;
    white-space: nowrap;
  }
  .headline-contact { left: 172px; top: 291px; }
  .services { position: absolute; left: 62px; top: 345px; list-style: none; }
  .service {
    display: flex; align-items: center; gap: 16px;
    height: 46px;
    font: 700 25px/1 "Poppins", sans-serif; white-space: nowrap;
  }
  .service-icon { width: 30px; height: 30px; flex: none; }
  .accent-line {
    position: absolute; left: 184px; top: 463px;
    width: 3px; height: 95px; background: var(--white);
  }
  .portrait-frame { position: absolute; left: 580px; top: 20px; width: 520px; height: 520px; }
</style>
</head>
<body>
  <section class="banner">
    <div class="brand-mark" aria-hidden="true"></div>
    <div class="brand-divider"></div>
    <p class="brand-name">Nordtal Finanzberatung GmbH</p>
    <p class="brand-tagline">Finanzieren, Versichern, Vorsorgen</p>

    <h1 class="headline">
      <span class="headline-small headline-your">Your</span>
      <span class="headline-regional">regional</span>
      <span class="headline-small headline-contact">contact at</span>
    </h1>

    <ul class="services">
      <li class="service">
        <svg class="service-icon" viewBox="0 0 30 30" fill="none" stroke="#fff" stroke-width="1.6" stroke-linejoin="round">
          <path d="M4 14 L15 5 L26 14"/>
          <path d="M7 12 V25 H23 V12"/>
          <rect x="12" y="17" width="6" height="8"/>
        </svg>
        Real estate and business financing
      </li>
      <li class="service">
        <svg class="service-icon" viewBox="0 0 30 30" fill="none" stroke="#fff" stroke-width="1.6" stroke-linejoin="round" stroke-linecap="round">
          <path d="M15 3 L24 6 V13 C24 19 20 23 15 25 C10 23 6 19 6 13 V6 Z"/>
          <path d="M11 14 L14 17 L19 11"/>
        </svg>
        Independent insurance advice
      </li>
    </ul>

    <div class="accent-line"></div>

    <svg class="portrait-frame" viewBox="0 0 520 520">
      <defs>
        <linearGradient id="photoTone" x1="0" y1="0" x2="1" y2="1">
          <stop offset="0" stop-color="#5a3a2e"/>
          <stop offset="0.5" stop-color="#c9b9ae"/>
          <stop offset="1" stop-color="#2a2f45"/>
        </linearGradient>
      </defs>
      <circle cx="258" cy="265" r="245" fill="#ffffff"/>
      <circle cx="278" cy="248" r="232" fill="#224b9c"/>
      <path d="M290 20 A236 236 0 0 1 505 245" fill="none" stroke="#ffffff" stroke-width="3"/>
      <circle cx="274" cy="253" r="211" fill="url(#photoTone)" role="img" aria-label="Portrait photo of the regional financial adviser in a dark suit and white shirt"/>
    </svg>
  </section>
</body>
</html>
```